Hearth Table Cover Design

Open to creative ideas, we don't have a set cover style in mind so have fun with it!
Front Cover for Ebook-Quorvex and vantor shelf. Book title is "Hearth Table" sub title is "A Gentle Map for Kitchen Rhythms", Author is Corinne L Waddell. Website is www.theolwynkitchenworks.com.
Open to creative ideas, we dont' have a set cover style in mind so have fun with it!
We have attached some pictures of Corinne which could be incorporated into the title. We can send you high def files if you need.
We have attached two book covers which we like to get you started, but feel free to have fun, we're looking for something creative and catchy

```html
<!DOCTYPE html>
<html lang="en">
<head>
<meta charset="utf-8">
<title>Hearth Table — Cover</title>
<link href="https://fonts.googleapis.com/css2?family=Arimo:wght@400&family=Quicksand:wght@400&family=Roboto:wght@300&display=swap" rel="stylesheet">
<style>
  :root {
    --peach: #f6b57f;
    --peach-text: #f2a565;
    --navy: #2d2b7c;
    --leaf: #2f7a34;
    --paper: #ffffff;
    --backdrop-top: #f4f2ef;
    --backdrop-bottom: #e4e1dc;
    --bark-light: #b7ada2;
    --bark-dark: #8f857a;
    --hair: #e6cf9e;
    --skin: #eec3a5;
    --shirt: #3f8a5c;
    --shirt-dark: #2f7049;
    --denim: #2f4a78;
  }
  html, body {
    margin: 0;
    padding: 0;
    width: 753px;
    height: 1200px;
    overflow: hidden;
    background: var(--paper);
  }
  .cover {
    position: relative;
    width: 753px;
    height: 1200px;
    background: var(--paper);
    overflow: hidden;
  }
  .band-top {
    position: absolute;
    left: 0; top: 0;
    width: 100%; height: 12px;
    background: var(--peach);
  }
  .title-bar {
    position: absolute;
    left: 0; top: 12px;
    width: 100%; height: 76px;
    display: flex;
    align-items: center;
    justify-content: center;
  }
  .title {
    margin: 0;
    font-family: "Arimo", Arial, sans-serif;
    font-weight: 400;
    font-size: 54px;
    letter-spacing: 2px;
    color: var(--navy);
    line-height: 1;
  }
  .rule {
    position: absolute;
    left: 0; top: 88px;
    width: 100%; height: 6px;
    background: var(--peach);
  }
  .backdrop {
    position: absolute;
    left: 0; top: 94px;
    width: 100%; height: 1006px;
    background: linear-gradient(180deg, var(--backdrop-top) 0%, var(--backdrop-bottom) 100%);
  }
  .tree {
    position: absolute;
    left: 0; top: 94px;
    width: 100px; height: 1006px;
    background: linear-gradient(90deg, var(--bark-dark) 0%, var(--bark-light) 70%, #cfc7bd 100%);
  }
  .figure {
    position: absolute;
    left: 90px; top: 110px;
    width: 420px; height: 990px;
    border-radius: 210px 210px 0 0;
    background: linear-gradient(180deg,
      var(--hair) 0%,
      var(--hair) 14%,
      var(--skin) 24%,
      var(--shirt) 36%,
      var(--shirt-dark) 76%,
      var(--skin) 82%,
      var(--skin) 90%,
      var(--denim) 95%,
      var(--denim) 100%);
  }
  .subtitle {
    position: absolute;
    right: 55px; top: 238px;
    margin: 0;
    width: 260px;
    text-align: right;
    font-family: "Roboto", Helvetica, sans-serif;
    font-weight: 300;
    font-size: 38px;
    line-height: 68px;
    color: var(--leaf);
  }
  .author-bar {
    position: absolute;
    left: 0; top: 1100px;
    width: 100%; height: 75px;
    background: var(--paper);
    display: flex;
    align-items: center;
    justify-content: center;
  }
  .author {
    margin: 0;
    font-family: "Quicksand", sans-serif;
    font-weight: 400;
    font-size: 52px;
    letter-spacing: 1px;
    color: var(--peach-text);
    line-height: 1;
  }
  .band-bottom {
    position: absolute;
    left: 0; bottom: 0;
    width: 100%; height: 25px;
    background: var(--peach);
  }
</style>
</head>
<body>
  <main class="cover">
    <div class="band-top"></div>
    <header class="title-bar">
      <h1 class="title">HEARTH TABLE</h1>
    </header>
    <div class="rule"></div>
    <section class="portrait" role="img" aria-label="Photograph of the author in a green cropped t-shirt and jeans, smiling, leaning against a pale tree trunk">
      <div class="backdrop"></div>
      <div class="tree"></div>
      <div class="figure"></div>
    </section>
    <p class="subtitle">a gentle<br>map for<br>kitchen<br>rhythms</p>
    <footer class="author-bar">
      <p class="author">corinne l. waddell</p>
    </footer>
    <div class="band-bottom"></div>
  </main>
</body>
</html>
```